Computer Repair Business - Needs New Business Card Design

I want to create a very cool business card for my business. I want to make it 100% different from my previous card. I would like to use similar color scheme like Royal blue.

With this card I want to create a conversation and have my customers say "Wow, that's a cool business card" Trying to prevent it from looking like the typical card that get's shoved into a wallet.

My website is below:

www.milospcworks.com

I want to edit the hours and website and email:

www.milospcworks.com
milo@milospcworks.com

10:30 to 6pm Monday - Friday
10:30 to 3pm Saturday

Just to remind, when i see a new design i don't want to notice my old design.

Business card will be printed and made with rounded corners and horizontal.

The back of the card should say " In-Store Repair, Remote Support, Data Recovery"

Industry/Entity Type

Business

Font styles to use
Sans Serif

Colors
33a6d7
3176b5

Requirements
Must have
• Clean looking - have creative aspects.
Should not have
• Should not look like the previous card design.

```html
<!DOCTYPE html>
<html lang="en">
<head>
<meta charset="utf-8">
<title>Milo's PC Works – Business Card</title>
<link rel="stylesheet" href="https://fonts.googleapis.com/css2?family=Open+Sans:wght@400;600;700&display=swap">
<style>
  :root {
    --backdrop: #1d1d1d;
    --card: #f7f7f7;
    --ink: #231f20;
    --muted: #3a3a3a;
    --royal: #3176b5;
    --sky: #33a6d7;
    --white: #ffffff;
  }
  * { margin: 0; padding: 0; box-sizing: border-box; }
  html, body { width: 1200px; height: 1000px; overflow: hidden; }
  body {
    background: var(--backdrop);
    font-family: "Open Sans", Arial, sans-serif;
    color: var(--ink);
    position: relative;
  }
  .card {
    position: absolute;
    left: 260px;
    width: 680px;
    height: 387px;
    background: var(--card);
    border-radius: 26px;
    overflow: hidden;
    box-shadow: 0 4px 14px rgba(0,0,0,.5);
  }
  .card--front { top: 85px; }
  .card--back { top: 528px; }

  .brand { position: absolute; }
  .brand__lockup {
    display: flex;
    align-items: center;
    justify-content: space-between;
  }
  .brand__words { white-space: nowrap; color: var(--ink); }
  .brand__name { display: block; font-weight: 600; }
  .brand__sub { display: block; font-weight: 400; text-transform: uppercase; color: var(--muted); }
  .brand__mark { background: var(--royal); flex: none; }
  .brand__rule { background: var(--ink); height: 1px; }
  .brand__tagline {
    font-weight: 700;
    text-transform: uppercase;
    white-space: nowrap;
  }

  .card--front .brand { left: 108px; top: 142px; width: 470px; }
  .card--front .brand__name { font-size: 58px; line-height: 56px; letter-spacing: 1px; }
  .card--front .brand__sub { font-size: 23px; line-height: 26px; letter-spacing: 6px; }
  .card--front .brand__mark { width: 74px; height: 74px; }
  .card--front .brand__rule { margin-top: 6px; }
  .card--front .brand__tagline { font-size: 17px; letter-spacing: 6.1px; margin-top: 10px; }

  .card--back .brand { left: 26px; top: 30px; width: 320px; }
  .card--back .brand__name { font-size: 40px; line-height: 38px; letter-spacing: .5px; }
  .card--back .brand__sub { font-size: 16px; line-height: 19px; letter-spacing: 4px; }
  .card--back .brand__mark { width: 50px; height: 50px; }
  .card--back .brand__rule { margin-top: 5px; }
  .card--back .brand__tagline { font-size: 12px; letter-spacing: 4.2px; margin-top: 10px; }

  .services {
    position: absolute;
    left: 26px;
    top: 172px;
    font-size: 16px;
    font-weight: 600;
    color: var(--royal);
    white-space: nowrap;
  }

  .contact-list {
    position: absolute;
    left: 26px;
    top: 260px;
    list-style: none;
    font-size: 17px;
    line-height: 23.5px;
  }
  .contact-list li { display: flex; align-items: center; gap: 8px; }
  .contact-list svg { width: 16px; height: 16px; fill: var(--royal); flex: none; }

  .address {
    position: absolute;
    left: 445px;
    top: 260px;
    font-style: normal;
  }
  .address__company { font-size: 19px; font-weight: 700; line-height: 26px; }
  .address__street { font-size: 18px; line-height: 24px; }
  .address__city { font-size: 15px; line-height: 20px; }

  .hours-band__accent {
    position: absolute;
    left: 0; right: 0;
    top: 342px;
    height: 4px;
    background: var(--sky);
  }
  .hours-band {
    position: absolute;
    left: 0; right: 0;
    top: 350px;
    bottom: 0;
    background: var(--royal);
    color: var(--white);
    display: flex;
    align-items: center;
    padding-left: 26px;
    font-size: 16px;
    white-space: nowrap;
  }
  .hours-band__dot { margin: 0 9px; }
  .partner-badge {
    display: inline-block;
    width: 150px;
    height: 18px;
    background: var(--white);
    opacity: .85;
    border-radius: 3px;
  }
</style>
</head>
<body>

<section class="card card--front" aria-label="Card front">
  <div class="brand">
    <div class="brand__lockup">
      <div class="brand__words">
        <span class="brand__name">MILO'S</span>
        <span class="brand__sub">PC Works</span>
      </div>
      <span class="brand__mark"></span>
    </div>
    <div class="brand__rule"></div>
    <div class="brand__tagline">Computer Repair &amp; Sales</div>
  </div>
</section>

<section class="card card--back" aria-label="Card back">
  <div class="brand">
    <div class="brand__lockup">
      <div class="brand__words">
        <span class="brand__name">MILO'S</span>
        <span class="brand__sub">PC Works</span>
      </div>
      <span class="brand__mark"></span>
    </div>
    <div class="brand__rule"></div>
    <div class="brand__tagline">Computer Repair &amp; Sales</div>
  </div>

  <p class="services">In-Store Repair, Remote Support, Data Recovery</p>

  <ul class="contact-list">
    <li>
      <svg viewBox="0 0 16 16" aria-hidden="true"><path d="M1 6c0-2 3-3.5 7-3.5S15 4 15 6v1.5h-3.5V6h-7v1.5H1zM3.5 8h9l1.5 6H2z"/></svg>
      555-014-2290
    </li>
    <li>
      <svg viewBox="0 0 16 16" aria-hidden="true"><path d="M1 3h14v10H1zm1.5 1.5v.3L8 9l5.5-4.2v-.3zm0 2.2v4.8h11V6.7L8 10.9z"/></svg>
      milo@milospcworks.com
    </li>
    <li>
      <svg viewBox="0 0 16 16" aria-hidden="true"><path d="M8 1a7 7 0 1 0 0 14A7 7 0 0 0 8 1zm0 1.3c.8.8 1.5 2.2 1.7 4h-3.4c.2-1.8.9-3.2 1.7-4zM5 6.3H2.4A5.7 5.7 0 0 1 5.8 2.7C5.4 3.7 5.1 4.9 5 6.3zm0 1.4c.1 1.4.4 2.6.8 3.6A5.7 5.7 0 0 1 2.4 7.7zm1.3 0h3.4c-.2 1.8-.9 3.2-1.7 4-.8-.8-1.5-2.2-1.7-4zm4.7 0h2.6a5.7 5.7 0 0 1-3.4 3.6c.4-1 .7-2.2.8-3.6zm0-1.4c-.1-1.4-.4-2.6-.8-3.6a5.7 5.7 0 0 1 3.4 3.6z"/></svg>
      www.milospcworks.com
    </li>
  </ul>

  <address class="address">
    <div class="address__company">Milo's PC Works</div>
    <div class="address__street">120 Harbor Road</div>
    <div class="address__city">Millbrook, NJ 07000</div>
  </address>

  <div class="hours-band__accent"></div>
  <div class="hours-band">
    <span>Mon - Fri: 10:30am - 6pm</span>
    <span class="hours-band__dot">•</span>
    <span>Saturday: 10:30am - 3pm</span>
    <span class="hours-band__dot">•</span>
    <span class="partner-badge" role="img" aria-label="Partner badge"></span>
  </div>
</section>

</body>
</html>
```